Velvora Style & Image Consultancy

Hi, I need a brochure design for my personal styling business. I have downloaded the company logo along with the content of the services offered for the brochure. Being a colour and styling business I would been keen on having some pictures of timeless fashion or colour samples, This is not absolutely necessary just an idea. I had also thought about changing and naming the services offered with a feminine, fun interesting type of theme. This may make it more inviting, I would be really interested in any of your creative ideas in this area. I will be deciding on the business card design in the next couple of days. I will download the design for this once I have made the decision. I will be okay to pay for any photo images that may be required if the brochure is selected. I had envisaged a tri fold brochure standard letter size with two folds (8.5" by 11inchs) however I am open to any suggestions. Please feel free to make any changes or modification's to the content, font etc in the files downloaded for the brochure. Many Thanks.
Updates
Project Deadline Extended
Reason: I need to extend the time for this project as I do not have all of content required for the brochure confirmed. Many Thanks
Industry/Entity Type
Fashion
Font styles to use
Look and feel
Each slider illustrates characteristics of the customer's brand and the style your logo design should communicate.

```html
<!DOCTYPE html>
<html lang="en">
<head>
<meta charset="utf-8">
<title>Velvora Style &amp; Image Consultancy – Styling Packages Brochure</title>
<link rel="stylesheet" href="https://fonts.googleapis.com/css2?family=Cinzel:wght@700&family=Berkshire+Swash&family=Mulish:wght@400;700;800&family=Oxygen:wght@300;400&display=swap">
<style>
  :root {
    --bg: #d8cdc0;
    --paper: #ffffff;
    --paper-tint: #eef5f7;
    --orange: #f2a81d;
    --orange-deep: #e0931a;
    --ink: #1e1e1e;
    --ink-soft: #4d4d4d;
    --rule: #f2c36a;
  }
  * { box-sizing: border-box; margin: 0; padding: 0; }
  html, body { width: 1200px; height: 960px; overflow: hidden; background: var(--bg); }
  .brochure {
    position: absolute; left: 30px; top: 40px;
    width: 1140px; height: 880px;
    display: grid; grid-template-columns: repeat(3, 1fr);
    box-shadow: 0 10px 30px rgba(0,0,0,.25);
  }
  .panel { position: relative; background: var(--paper); overflow: hidden; }
  .panel + .panel { border-left: 1px solid #e6e6e6; }
  .panel--tint { background: var(--paper-tint); }

  .banner {
    display: inline-block; position: relative;
    background: var(--orange); color: var(--ink);
    font: 700 19px/1 "Cinzel", serif; letter-spacing: .5px;
    padding: 9px 34px 9px 14px;
    clip-path: polygon(0 0, calc(100% - 16px) 0, 100% 50%, calc(100% - 16px) 100%, 0 100%);
  }
  .banner--caps { text-transform: uppercase; }

  .package-title {
    font: 400 17px/1.2 "Berkshire Swash", cursive; color: var(--orange-deep);
    margin-bottom: 8px;
  }
  .package-intro {
    font: 700 12.5px/1.45 "Mulish", sans-serif; color: var(--ink);
    text-align: justify; padding-bottom: 10px;
    border-bottom: 1.5px solid var(--rule);
  }
  .service-list { list-style: none; margin: 14px 0 16px; }
  .service-list li {
    display: grid; grid-template-columns: 30px 1fr; align-items: start;
    font: 300 15px/1.15 "Oxygen", sans-serif; color: var(--ink-soft);
    margin-bottom: 12px;
  }
  .service-list .num { font: 400 17px/1 "Oxygen", sans-serif; color: var(--ink); }
  .price { font: 400 15px/1.25 "Oxygen", sans-serif; color: var(--ink); }
  .price small { display: block; font-size: 14px; }

  .panel-body { padding: 0 28px; }
  .panel--one .banner { margin: 44px 0 24px; }
  .photo-frame { position: absolute; left: 20px; right: 20px; bottom: 0; height: 300px; }

  .photo-top { height: 250px; background: linear-gradient(135deg, #c9b59e, #e9d3a8 45%, #8aa7c4); }
  .panel--two .panel-body { padding-top: 28px; }

  .panel--three .panel-body { padding-top: 30px; }
  .lifestyle .banner { margin: 8px 0 18px -28px; padding-left: 28px; }
  .lifestyle-copy {
    font: 700 12.5px/1.5 "Mulish", sans-serif; color: var(--ink); text-align: justify;
  }
  .photo-rack {
    position: absolute; left: 28px; right: 0; bottom: 0; height: 250px;
    border-top: 5px solid var(--orange); border-left: 5px solid var(--orange);
    background: linear-gradient(120deg, #7a3b52, #c6506b 30%, #3b5d8c 60%, #e7dccd);
  }
</style>
</head>
<body>
<main class="brochure" aria-label="Velvora Style &amp; Image Consultancy styling packages">

  <section class="panel panel--one">
    <div class="panel-body">
      <h1 class="banner">Premium Styling Packages</h1>
      <h2 class="package-title">Special Occasion Style Me Beautiful Package</h2>
      <p class="package-intro">This is a great experience for weddings, birthdays, or just wanting to look your absolute best for any occasion. Treat someone special to the ultimate gift. Gift vouchers &amp; before and after photos available on request.</p>
      <ol class="service-list">
        <li><span class="num">1</span>Consultation</li>
        <li><span class="num">2</span>Personal shopping service</li>
        <li><span class="num">3</span>Hair (accompaniment to hair salon)</li>
        <li><span class="num">4</span>Make up Make over</li>
      </ol>
      <p class="price">Price $ 185.00<small>(This does not include cost of hair salon)</small></p>
    </div>
    <svg class="photo-frame" viewBox="0 0 340 300" preserveAspectRatio="none" role="img" aria-label="Photo of a woman in a beige trench coat holding a green handbag">
      <defs>
        <linearGradient id="coatTones" x1="0" y1="0" x2="1" y2="1">
          <stop offset="0" stop-color="#f6ecdf"/>
          <stop offset=".6" stop-color="#d9bf9c"/>
          <stop offset="1" stop-color="#7fb8a0"/>
        </linearGradient>
      </defs>
      <polygon points="40,10 250,10 330,90 330,300 2,300 2,50" fill="url(#coatTones)" stroke="#f2a81d" stroke-width="2"/>
    </svg>
  </section>

  <section class="panel panel--two">
    <div class="photo-top" role="img" aria-label="Photo of two women walking and shopping together"></div>
    <div class="panel-body">
      <h2 class="package-title">The Forever Gorgeous Package</h2>
      <p class="package-intro">Discover and Shine with a new signature style. This package will empower you with the confidence to dress for success every day.</p>
      <ol class="service-list">
        <li><span class="num">1</span>Style &amp; Colour Consultation</li>
        <li><span class="num">2</span>Personal Shopping Service</li>
        <li><span class="num">3</span>Make up Lesson</li>
        <li><span class="num">4</span>Style me complete consultation (accessories &amp; shoes)</li>
        <li><span class="num">5</span>Hair (accompaniment to hair salon)</li>
      </ol>
      <p class="price">Price $ 185.00<small>(This does not include cost of hair salon)</small></p>
    </div>
  </section>

  <section class="panel panel--tint panel--three">
    <div class="panel-body">
      <h2 class="package-title">The Ultimate Wardrobe Makeover Package</h2>
      <p class="package-intro">This will provide you with a freedom to dress effortlessly for any occasion. Relax and enjoy a functional well-coordinated wardrobe that reflects you and your lifestyle. Discover how to dress without the stress.</p>
      <ol class="service-list">
        <li><span class="num">1</span>Wardrobe clear out/reassess</li>
        <li><span class="num">2</span>Style &amp; colour complete consultation (accessories &amp; shoes)</li>
      </ol>
      <p class="price">Price $365.00</p>
      <div class="lifestyle">
        <h2 class="banner banner--caps">Dress for the life you love</h2>
        <p class="lifestyle-copy">Time for a change, take a fresh look and discover how to dress in a style that reflects your personality &amp; lifestyle. Be confident, look amazing &amp; feel great about the way that you look every day. Some people always look effortlessly stylish, looking good is all about knowing what suits you.</p>
      </div>
    </div>
    <div class="photo-rack" role="img" aria-label="Photo of a woman browsing a rail of colourful clothes"></div>
  </section>

</main>
</body>
</html>
```